Walk Bold Stay Kind Ebook and Print book cover

I need a professional, eye catching cover that will stand out. The title of the book is "Walk Bold Stay Kind: 47 Quiet Rules For Calm and Wonder" It is a self-help personal transformation book by author Dale Ormsby. The cover will be on both print and ebook covers. I want something that is similar yet different to best-selling books in the genre, nothing too boring. A blue background might work, but it isn't a requirement. I'm open to other colors as long as it's powerful, professional, and screams "Buy me because this book is going to change your life!"
Updates

So far, 3 designs (3 of the 4 star rated designs) are in contention, but they all can be improved. I think the book cover should best convey "thinking smart" in a dynamic way. I'll run another poll in a day or so when I get additional designs I like. Added Thursday, May 4, 2017

Based on current designs, I wanted to provide additional guidance. The title and image should pop and be clearly visible at a distance as a thumbnail. Also, I'm wanting something bold and creative but not too confusing. I currently have a couple solid designs that are in contention to win, but I have another 7 days left for the project. I extended it to 10 days from the initial 5. I'll include several more polls for my followers and will likely pick the top ranking design based off the series of polls and will be eliminating lower ranking designs with each new poll and set of promising designs that come in. Finally, I may ask to see what the back will look like on the print version since I'll need both the Lumora and print (5" by 8") designs. Added Saturday, May 6, 2017

It's been recommended by some that I should have my own picture on the cover. I'm not completely convinced, but I would like to see some additional designs that incorporate my photo (touched up to remove the shine from my forehead and the label brand name removed from the t-shire) into a cover design. I have several good designs coming in, so typeset and professional looking font is extremely important. Blue is also preferred but not required. I've attached the photo on the brief for those who want to submit a design with that photo. Added Saturday, May 6, 2017

Target Market(s)

Working age adults seeking personal transformation and self improvement.

Industry/Entity Type

Motivation

Requirements
Must have
• Creativity. Eye catching. Striking. Contrast. Looks good close up and as a thumbnail at a distance. Font should be easy to read and pop from the cover along with the design.
Nice to have
• Powerful image placement. Play up the "Walk Bold" aspect of the title. Perhaps even contrasting someone who's thinking "Hard." Here are a few examples of intriguing covers (though not necessarily related to the genre) I like mainly for aesthetics and creativity. https://www.shopvale.com/dp/Q71MRT2KWD/ https://www.shopvale.com/dp/Q34PLN8XEA
• https://www.shopvale.com/dp/Q925GHV3TC/
• https://www.shopvale.com/dp/Q48DJW6RZB/
• (the font is a little poor in the last one but the image is evoking)
Should not have
• Ugly, tacky, or hard to read fonts. A simple photo with text on top. A simple background with words. Confusing images. Designs with no additional stock image purchase requirements will be given preference over those that do. I've seen a lot of balloons and light bulbs. I'm not saying you can't include them in the design, but if you want to stand out, try to find something more creative that expresses the concept of the title.

```html
<!DOCTYPE html>
<html lang="en">
<head>
<meta charset="utf-8">
<title>Walk Bold Stay Kind — Dale Ormsby</title>
<link rel="stylesheet" href="https://fonts.googleapis.com/css2?family=Montserrat:wght@700;800;900&display=swap">
<style>
  :root {
    --board-light: #5e6063;
    --board-mid: #434548;
    --board-dark: #2a2b2d;
    --chalk-white: #f1f1ee;
    --accent-yellow: #f2c230;
    --fog: #ffffff;
    --author-ink: #3b3c3e;
    --skin-tone: #c79a7c;
    --shirt-navy: #1f2433;
    --flag-blue: #3d5a8c;
    --flag-red: #9a3b3b;
    --chalk-arm: #9a9c9f;
  }
  html, body {
    margin: 0;
    padding: 0;
    width: 750px;
    height: 1200px;
    overflow: hidden;
    background: var(--board-dark);
  }
  .cover {
    position: relative;
    width: 750px;
    height: 1200px;
    overflow: hidden;
    font-family: "Montserrat", "Arial Black", sans-serif;
    background:
      radial-gradient(ellipse 70% 45% at 50% 40%, var(--board-light) 0%, rgba(94,96,99,0) 100%),
      linear-gradient(180deg, var(--board-mid) 0%, var(--board-dark) 55%, var(--board-mid) 100%);
  }
  .cover__title {
    position: absolute;
    top: 64px;
    left: 0;
    width: 100%;
    margin: 0;
    text-align: center;
    font-weight: 900;
    font-size: 96px;
    line-height: 114px;
    letter-spacing: 2px;
    text-transform: uppercase;
    color: var(--chalk-white);
  }
  .cover__title-line { display: block; }
  .cover__title .is-accent { color: var(--accent-yellow); }
  .cover__subtitle {
    position: absolute;
    top: 340px;
    left: 0;
    width: 100%;
    margin: 0;
    text-align: center;
    font-weight: 800;
    font-size: 32px;
    line-height: 38px;
    letter-spacing: 1px;
    text-transform: uppercase;
    color: var(--chalk-white);
  }
  .cover__portrait {
    position: absolute;
    left: 42px;
    top: 436px;
    width: 666px;
    height: 764px;
    border-radius: 46% 46% 0 0 / 16% 16% 0 0;
    background:
      radial-gradient(ellipse 10% 10% at 50% 9%, var(--skin-tone) 0%, var(--skin-tone) 70%, rgba(199,154,124,0) 100%),
      radial-gradient(ellipse 22% 16% at 50% 42%, var(--flag-blue) 0%, rgba(61,90,140,0) 100%),
      linear-gradient(180deg, rgba(0,0,0,0) 48%, var(--flag-red) 52%, rgba(154,59,59,0) 60%),
      linear-gradient(90deg, var(--chalk-arm) 0%, #6f7174 22%, var(--shirt-navy) 24%, var(--shirt-navy) 76%, #6f7174 78%, var(--chalk-arm) 100%);
  }
  .cover__fog {
    position: absolute;
    left: 0;
    bottom: 0;
    width: 100%;
    height: 440px;
    background: linear-gradient(180deg, rgba(255,255,255,0) 0%, rgba(255,255,255,0.6) 30%, var(--fog) 62%);
  }
  .cover__author {
    position: absolute;
    top: 1098px;
    left: 0;
    width: 100%;
    margin: 0;
    text-align: center;
    font-weight: 800;
    font-size: 44px;
    line-height: 54px;
    letter-spacing: 2px;
    text-transform: uppercase;
    color: var(--author-ink);
  }
</style>
</head>
<body>
  <main class="cover">
    <h1 class="cover__title">
      <span class="cover__title-line">Walk <span class="is-accent">Bold</span></span>
      <span class="cover__title-line"><span class="is-accent">Stay</span> Kind</span>
    </h1>
    <p class="cover__subtitle">47 Quiet Rules For<br>Calm and Wonder</p>
    <div class="cover__portrait" role="img" aria-label="Author portrait photo in a dark star-and-stripe t-shirt, with chalk-drawn flexing arms sketched on the board behind him"></div>
    <div class="cover__fog"></div>
    <p class="cover__author">Dale Ormsby</p>
  </main>
</body>
</html>
```